Bold and colurful E-liquid Design Template

I'm looking for a new label for my house range of vape e-liquids. I currently have almost 40 flavours, so I'm looking for a single label design that I can modify to create the rest of the flavours.
Each label will have the same design, but I'll change the color for each flavour and the name.
I'd like the label to be predominantly text based with bold text and bold colours. I like bold typographic styles. Also for each flavour I'd like to add 1 - 3 letters to represent the flavour. This can be in a larger font.
eg for
Blueberry I'll use the letter B
Pineapple Peach will use PP
Cinnamon Blueberry Muffin uses CBM
The colour used on the label will also be important so they stand out nicely on the shelf.
I've attached a psd mockup of the bottles I'll be using.

```html
<!DOCTYPE html>
<html lang="en">
<head>
<meta charset="utf-8">
<title>Vape Liquid Label Range</title>
<link rel="stylesheet" href="https://fonts.googleapis.com/css2?family=Germania+One&family=Montserrat:wght@500;600&display=swap">
<style>
  :root {
    --page: #f1f1f1;
    --silver: #e6ebee;
    --silver-mid: #c4cbd0;
    --gold: #d9a545;
    --blue-light: #2c3fb0;
    --blue-deep: #141c78;
    --blue-tab: #1f3a9e;
    --orange-light: #ec7a4c;
    --orange-deep: #c8552a;
    --orange-tab: #8f2a12;
  }
  * { box-sizing: border-box; margin: 0; padding: 0; }
  html, body { width: 738px; height: 1200px; overflow: hidden; background: var(--page); }
  .range {
    width: 738px; height: 1200px;
    display: flex; justify-content: center; align-items: center; gap: 42px;
  }
  .label {
    position: relative;
    width: 230px; height: 640px;
    border-top: 4px solid var(--gold);
    border-bottom: 4px solid var(--gold);
    overflow: hidden;
    display: flex; flex-direction: column; align-items: center;
  }
  .label--blueberry { background: linear-gradient(160deg, var(--blue-light), var(--blue-deep) 70%); --tab: var(--blue-tab); }
  .label--pineapple-peach {
    background:
      radial-gradient(circle, rgba(255,220,160,.25) 1px, transparent 1.5px) 0 0 / 8px 8px,
      linear-gradient(160deg, var(--orange-light), var(--orange-deep) 75%);
    --tab: var(--orange-tab);
  }
  .flavour-mark {
    width: 180px; height: 250px; margin-top: 44px;
    border-radius: 90px 90px 90px 90px / 110px 110px 90px 90px;
    background: radial-gradient(ellipse at 50% 55%, var(--silver), var(--silver-mid) 60%, rgba(196,203,208,.35) 100%);
    opacity: .85;
  }
  .title {
    margin-top: 34px;
    font-family: "Germania One", serif;
    font-weight: 400;
    font-size: 80px; line-height: .88;
    text-align: center; color: var(--silver);
    letter-spacing: 1px;
  }
  .tagline {
    margin-top: 14px;
    font-family: "Montserrat", sans-serif; font-weight: 500;
    font-size: 11px; letter-spacing: 1.2px;
    color: var(--silver);
    white-space: nowrap;
  }
  .net {
    position: absolute; bottom: 0; left: 20px; right: 20px; height: 50px;
    background: var(--tab);
    border-top: 2px solid var(--silver);
    border-radius: 14px 14px 0 0;
    display: flex; align-items: center; justify-content: center;
    font-family: "Montserrat", sans-serif; font-weight: 600;
    font-size: 17px; color: #fff;
  }
</style>
</head>
<body>
<main class="range">
  <section class="label label--blueberry">
    <div class="flavour-mark" role="img" aria-label="Silver flavour monogram with flame and ring"></div>
    <h2 class="title">VAPE<br>LIQUID</h2>
    <p class="tagline">FOR ALL VAPER DEVICES</p>
    <div class="net">NET WT. 60 ML</div>
  </section>
  <section class="label label--pineapple-peach">
    <div class="flavour-mark" role="img" aria-label="Silver flavour monogram with flame and ring"></div>
    <h2 class="title">VAPE<br>LIQUID</h2>
    <p class="tagline">FOR ALL VAPING DEVICES</p>
    <div class="net">NET WT. 60 ML</div>
  </section>
</main>
</body>
</html>
```